Vértice Lunar Presentation

We already have a logo, and now we need a good presentation for our company. You can seach for us at : verticelunar.pt and see more about us. We work in adaptive reuse of buildings. You can ask anything you need to do a great job.

Industry/Entity Type

It Company

```html
<!DOCTYPE html>
<html lang="pt">
<head>
<meta charset="utf-8">
<title>Vértice Lunar — Apresentação</title>
<link href="https://fonts.googleapis.com/css2?family=Fira+Sans:wght@400;700&display=swap" rel="stylesheet">
<style>
:root{
  --blue:#0c6fc2;
  --blue-mid:#2d86d6;
  --blue-light:#5aa6e6;
  --navy:#0b3f7c;
  --ink:#555;
  --grey:#b9b9b9;
  --grey-dark:#7a7a7a;
  --row-a:#e3e8f2;
  --row-b:#c9d3e6;
  --footer:#e4e4e4;
}
*{margin:0;padding:0;box-sizing:border-box}
html,body{width:1200px;height:681px;overflow:hidden;background:#fff}
body{position:relative;font-family:"Fira Sans",Arial,sans-serif;color:var(--ink)}
.slide{position:absolute;width:378px;height:283px;background:#fff;overflow:hidden;
  box-shadow:2px 3px 5px rgba(0,0,0,.35);border:1px solid #ddd}
.slide--cover{background:linear-gradient(#f4f4f4,#dedede 35%,#cfcfcf 70%,#e8e8e8)}
.cover-band{position:absolute;left:0;right:0;top:94px;height:100px;background:#bfbfbf}
.brand{position:absolute;left:10px;top:12px;display:flex;align-items:center;gap:4px;
  color:var(--navy);font-weight:700;font-size:11px}
.brand-dot{width:12px;height:12px;border-radius:50%;background:var(--navy)}
.tablet{position:absolute;left:42px;top:41px;width:292px;height:221px;border-radius:14px;
  background:linear-gradient(#3a3a3a,#111);box-shadow:0 10px 14px rgba(0,0,0,.3)}
.screen{position:absolute;left:20px;top:16px;width:256px;height:184px;overflow:hidden;
  background:linear-gradient(#8ab7e6 0%,#b9d3ea 35%,#d9d2c4 55%,#8d8a7c 78%,#5a6a4a 100%)}
.screen .divider{position:absolute;top:0;bottom:0;width:3px;background:#fff}
.screen .title-band{position:absolute;left:0;right:0;top:136px;height:26px;background:var(--blue);
  color:#fff;font-size:17px;line-height:26px;padding-left:4px}
.screen .sub{position:absolute;left:4px;top:165px;color:#fff;font-size:11px}
.head{position:absolute;top:16px;left:0;height:27px;background:var(--blue);color:#fff;
  font-size:17px;line-height:27px;padding-left:14px}
.footer{position:absolute;left:0;right:0;bottom:0;height:19px;background:linear-gradient(#f2f2f2,var(--footer));
  font-size:5.5px;color:#777;line-height:19px}
.footer span{position:absolute}
.footer .rule{top:3px;width:1px;height:13px;background:var(--blue)}
.footer .mini{right:8px;display:flex;align-items:center;gap:2px;color:var(--navy);font-weight:700;font-size:6px}
.footer .mini i{width:6px;height:6px;border-radius:50%;background:var(--navy)}
.donut{position:absolute;top:64px;width:100px;height:100px}
.hr{position:absolute;left:0;right:0;height:1px;background:#9fb7d6}
.col{position:absolute;top:179px;width:104px;font-size:6px;line-height:7.6px;color:#555}
.vrule{position:absolute;top:178px;height:60px;width:1px;background:var(--blue)}
.bullets{position:absolute;left:16px;top:52px;width:194px;font-size:8px;line-height:8.6px;color:#666;list-style:none}
.bullets li{position:relative;padding-left:11px;margin-bottom:5px}
.bullets li::before{content:"";position:absolute;left:0;top:1px;width:2px;height:7px;background:var(--blue)}
.bullets ul{list-style:none;margin-top:5px;font-size:7px;line-height:7.6px}
.bullets ul li{padding-left:16px;margin-bottom:4px}
.bullets ul li::before{left:3px;top:3px;width:6px;height:1px}
.photo{position:absolute;left:217px;top:44px;width:161px;height:220px;
  background:linear-gradient(135deg,#c9ac82,#9c7a55 45%,#5a4a3a 70%,#c2a47a)}
.table-title{position:absolute;top:64px;left:0;right:0;text-align:center;font-size:12px;color:#666}
table{position:absolute;left:25px;top:94px;width:326px;border-collapse:collapse;font-size:7px;text-align:center}
td,th{height:15px;border:1px solid #fff}
th{background:var(--blue);color:#fff;font-weight:700}
tr:nth-child(odd) td{background:var(--row-b)}
tr:nth-child(even) td{background:var(--row-a)}
tr.total td{background:var(--blue);color:#fff;font-weight:700}
</style>
</head>
<body>

<!-- Cover -->
<section class="slide slide--cover" style="left:15px;top:51px">
  <div class="cover-band"></div>
  <div class="brand"><span class="brand-dot"></span>Vértice Lunar</div>
  <div class="tablet">
    <div class="screen" role="img" aria-label="Fotografia de edifício histórico numa praça urbana">
      <span class="divider" style="left:69px"></span>
      <span class="divider" style="left:179px"></span>
      <div class="title-band">Título da apresentação</div>
      <div class="sub">Subtítulo e / ou orador</div>
    </div>
  </div>
</section>

<!-- Charts -->
<section class="slide" style="left:405px;top:51px">
  <div class="head" style="width:219px">Título do slide de gráficos</div>
  <svg width="0" height="0" style="position:absolute">
    <defs>
      <g id="ring">
        <circle cx="50" cy="50" r="38" fill="none" stroke="#ddd" stroke-width="1"/>
        <g transform="rotate(-90 50 50)" fill="none" stroke-width="12">
          <circle cx="50" cy="50" r="38" pathLength="100" stroke="#0c6fc2" stroke-dasharray="30.6 100"/>
          <circle cx="50" cy="50" r="38" pathLength="100" stroke="#0b3f7c" stroke-dasharray="20.4 100" stroke-dashoffset="-30.6"/>
          <circle cx="50" cy="50" r="38" pathLength="100" stroke="#2d86d6" stroke-dasharray="7.1 100" stroke-dashoffset="-51"/>
          <circle cx="50" cy="50" r="38" pathLength="100" stroke="#5aa6e6" stroke-dasharray="6.1 100" stroke-dashoffset="-58.1"/>
          <circle cx="50" cy="50" r="38" pathLength="100" stroke="#b9b9b9" stroke-dasharray="15.3 100" stroke-dashoffset="-64.2"/>
          <circle cx="50" cy="50" r="38" pathLength="100" stroke="#7a7a7a" stroke-dasharray="10.2 100" stroke-dashoffset="-79.5"/>
          <circle cx="50" cy="50" r="38" pathLength="100" stroke="#111" stroke-dasharray="10.3 100" stroke-dashoffset="-89.7"/>
        </g>
        <circle cx="50" cy="50" r="27" fill="none" stroke="#ddd" stroke-width="2"/>
        <circle cx="50" cy="50" r="22" fill="#9a9a9a"/>
        <g font-size="6" fill="#fff" font-family="Fira Sans, sans-serif" text-anchor="middle">
          <text x="82" y="38">6</text><text x="74" y="82">4</text><text x="50" y="88">1,4</text>
          <text x="38" y="82">1,2</text><text x="16" y="57">3</text><text x="20" y="32">2</text><text x="43" y="18">2</text>
        </g>
      </g>
    </defs>
  </svg>
  <svg class="donut" style="left:12px" viewBox="0 0 100 100"><use href="#ring"/>
    <circle cx="50" cy="47" r="6" fill="none" stroke="#fff" stroke-width="1.5"/><rect x="47" y="53" width="6" height="4" fill="#fff"/></svg>
  <svg class="donut" style="left:138px" viewBox="0 0 100 100"><use href="#ring"/>
    <circle cx="50" cy="42" r="3.5" fill="#fff"/><path d="M46 60h8l-2-14h-4z" fill="#fff"/></svg>
  <svg class="donut" style="left:265px" viewBox="0 0 100 100"><use href="#ring"/>
    <path d="M55 38l5 5-12 12-6 1 1-6z" fill="#fff"/></svg>
  <div class="hr" style="top:167px"></div>
  <div class="col" style="left:22px">Lorem ipsum dolor sit amet, consectetur adipiscing elit. Curabitur eros turpis, laoreet nec nisi quis, pretium imperdiet turpis. Cras nisi orci, pulvinar vitae lectus vel, porta fermentum enim. Suspendisse sit amet malesuada tellus.</div>
  <div class="vrule" style="left:128px"></div>
  <div class="col" style="left:149px">Lorem ipsum dolor sit amet, consectetur adipiscing elit. Curabitur eros turpis, laoreet nec nisi quis, pretium imperdiet turpis. Cras nisi orci, pulvinar vitae lectus vel, porta fermentum enim. Suspendisse sit amet malesuada tellus.</div>
  <div class="vrule" style="left:255px"></div>
  <div class="col" style="left:275px">Lorem ipsum dolor sit amet, consectetur adipiscing elit. Curabitur eros turpis, laoreet nec nisi quis, pretium imperdiet turpis. Cras nisi orci, pulvinar vitae lectus vel, porta fermentum enim. Suspendisse sit amet malesuada tellus.</div>
  <div class="hr" style="top:246px"></div>
  <div class="footer"><span style="left:14px">15-06-2014</span><span class="rule" style="left:106px"></span>
    <span style="left:158px">Confidencial</span><span class="rule" style="left:244px"></span><span style="left:252px">2</span>
    <span class="mini"><i></i>Vértice Lunar</span></div>
</section>

<!-- Text and image -->
<section class="slide" style="left:798px;top:51px">
  <div class="head" style="width:378px">Título do slide de texto e imagens</div>
  <ul class="bullets">
    <li>Lorem ipsum dolor sit amet, consectetur adipiscing elit.
      <ul><li>Curabitur eros turpis, laoreet nec nisi quis, pretium imperdiet turpis.</li>
      <li>Cras nisi orci, pulvinar vitae lectus vel, porta fermentum enim. Suspendisse sit amet malesuada tellus.</li></ul></li>
    <li>Lorem ipsum dolor sit amet, consectetur adipiscing elit. Curabitur eros turpis, laoreet nec nisi quis, pretium imperdiet turpis.
      <ul><li>Cras nisi orci, pulvinar vitae lectus vel, porta fermentum enim. Suspendisse sit amet malesuada tellus.</li></ul></li>
    <li>Lorem ipsum dolor sit amet, consectetur adipiscing elit. Curabitur eros turpis, laoreet nec nisi quis, pretium imperdiet turpis.
      <ul><li>Cras nisi orci, pulvinar vitae lectus vel, porta fermentum enim. Suspendisse sit amet malesuada tellus.</li></ul></li>
  </ul>
  <div class="photo" role="img" aria-label="Fotografia de janela com varanda em fachada de pedra"></div>
  <div class="footer"><span style="left:14px">15-06-2014</span><span class="rule" style="left:106px"></span>
    <span style="left:158px">Confidencial</span><span class="rule" style="left:244px"></span><span style="left:252px">3</span>
    <span class="mini"><i></i>Vértice Lunar</span></div>
</section>

<!-- Table -->
<section class="slide" style="left:15px;top:369px">
  <div class="head" style="width:205px">Título do slide de tabela</div>
  <div class="table-title">Titulo da tabela</div>
  <table>
    <thead><tr><th>Tópico 1</th><th>Tópico 2</th><th>Tópico 3</th><th>Tópico 4</th><th>Tópico 5</th><th>Tópico 6</th></tr></thead>
    <tbody>
      <tr><td>458</td><td>124</td><td>258</td><td>556</td><td>850</td><td>245</td></tr>
      <tr><td>327</td><td>785</td><td>778</td><td>165</td><td>462</td><td>247</td></tr>
      <tr><td>123</td><td>332</td><td>251</td><td>330</td><td>782</td><td>310</td></tr>
      <tr><td>854</td><td>147</td><td>468</td><td>654</td><td>334</td><td>957</td></tr>
      <tr><td>954</td><td>963</td><td>493</td><td>321</td><td>569</td><td>577</td></tr>
      <tr class="total"><td>335</td><td>547</td><td>937</td><td>410</td><td>445</td><td>950</td></tr>
    </tbody>
  </table>
  <div class="footer"><span style="left:14px">15-06-2014</span><span class="rule" style="left:106px"></span>
    <span style="left:158px">Confidencial</span><span class="rule" style="left:244px"></span><span style="left:252px">4</span>
    <span class="mini"><i></i>Vértice Lunar</span></div>
</section>

<!-- Closing -->
<section class="slide slide--cover" style="left:405px;top:369px">
  <div class="cover-band"></div>
  <div class="brand"><span class="brand-dot"></span>Vértice Lunar</div>
  <div class="tablet">
    <div class="screen" role="img" aria-label="Fotografia de edifício histórico numa praça urbana">
      <span class="divider" style="left:69px"></span>
      <span class="divider" style="left:179px"></span>
      <div class="title-band">THANK YOU</div>
      <div class="sub">FOR YOUR TIME</div>
    </div>
  </div>
</section>

</body>
</html>
```